Flyer - Crestline Dental Marbury

** Please do not use my words - word-for-word on the flyer design **
We have recently bought an established dental business. However we are not getting new customers through the door. We plan to implement aggressive local marketing strategies including flyer distribution. We are looking for an eye-catching must read flyer design. Some details & content ideas are as below.
1. A5 size - Double Sided
2. Our business name is Crestline Dental Marbury. Logo is attached. Website is www.crestlinedentalmarbury.com.au where lot of useful information can be found.
3. Practice has a long & proud history serving "Lower North Shore" since 1958. We provide quality dental care at affordable prices.
4. List of services can be found on website
5. Perhaps a snippet of Orbisa Map Location would be useful. Also the fact that 3-hour free parking is available in Fernleigh Arcade less than 100m away from practice. Plenty of 2-hours street parking is available too.
6. Opening hours can be found on website. Fact that we are open on Saturdays and till late on Tuesdays is worth calling out.
7. We would like to run a campaign of offers with this flyer. Give it a name! Details below.
a) NO GAP Checkup and Clean with any major Private Health Fund. Includes oral exam, 2 X-Rays, Scale & Polish and Fluoride Treatment
b) Genuine Teeth Whitening for $199 (usually $399 save $200)
c) 10% off on all major dental. Includes fillings, crowns, bridges and root canal treatment
8. We are KELMA Preferred Provider means KELMA members get maximum benefit. KELMA Patron Plus logo attached.
9. We participate in Office of Ranger Welfare Fee Schedule. Logo attached.
10. Call out WE ACCEPT ALL HEALTH FUNDS
Dental
- Helvetica Neue, Myriad Pro

```html
<!DOCTYPE html>
<html lang="en">
<head>
<meta charset="utf-8">
<title>Crestline Dental Marbury – Flyer</title>
<link href="https://fonts.googleapis.com/css2?family=Arimo:wght@400;700&family=Oswald:wght@500;600&display=swap" rel="stylesheet">
<style>
  :root {
    --teal: #4fb795;
    --teal-dark: #2b8c6c;
    --green: #9fcb3b;
    --green-light: #bcdc55;
    --green-olive: #7da43a;
    --text-grey: #555555;
    --text-dark: #222222;
    --tick-red: #e0262b;
    --stage: #2a2a2a;
    --paper: #ffffff;
    --panel-grey: #e6e6e6;
  }
  * { margin: 0; padding: 0; box-sizing: border-box; }
  html, body { width: 900px; height: 1200px; overflow: hidden; }
  body { background: var(--stage); font-family: "Arimo", Arial, sans-serif; position: relative; }

  .flyer {
    position: absolute; left: 45px; top: 88px; width: 803px; height: 1037px;
    background: var(--paper); overflow: hidden;
    box-shadow: 0 6px 18px rgba(0,0,0,.5);
  }
  .hero-photo {
    position: absolute; left: 0; top: 0; width: 803px; height: 460px;
    background: linear-gradient(100deg, #bcd9ee 0%, #e6f0f5 18%, #f3d6cc 35%, #f0bdb0 55%, #f7e4dc 75%, #fbf3ef 100%);
  }
  .hero-shapes { position: absolute; left: 0; top: 0; width: 803px; height: 1037px; }

  .brand {
    position: absolute; left: 512px; top: 40px; display: flex; align-items: center; gap: 10px;
  }
  .brand-dot { width: 26px; height: 26px; border-radius: 50%; background: var(--green); flex: none; }
  .brand-name {
    font-weight: 700; font-size: 26px; line-height: 30px; color: var(--teal); width: 250px;
  }

  .headline {
    position: absolute; right: 24px; top: 158px; text-align: right;
    font-weight: 700; font-size: 49px; line-height: 51px; color: var(--teal);
    text-shadow: 2px 2px 2px rgba(0,0,0,.35);
  }

  .offer-banner {
    position: absolute; left: 190px; top: 362px; width: 428px; height: 64px;
    background: linear-gradient(180deg, var(--green-light), var(--green));
    color: var(--teal-dark); font-weight: 700; font-size: 22px; line-height: 24px;
    text-align: center; padding-top: 8px;
    box-shadow: 0 8px 8px -4px rgba(0,0,0,.35);
  }

  .intro { position: absolute; left: 0; width: 803px; text-align: center; color: var(--text-grey); }
  .intro-gap { top: 447px; font-size: 17px; line-height: 23px; }
  .intro-family { top: 504px; font-size: 17.5px; line-height: 25px; padding: 0 20px; }

  .promise {
    position: absolute; left: 0; top: 594px; width: 803px; text-align: center;
    font-family: "Oswald", "Arial Narrow", sans-serif; font-weight: 600; font-size: 27px;
    color: var(--green-olive); text-shadow: 1px 1px 1px rgba(0,0,0,.35); letter-spacing: .3px;
  }

  .hours-tag {
    position: absolute; left: 38px; top: 653px; width: 182px; height: 31px;
    background: linear-gradient(180deg, #6cc9a6, var(--teal-dark)); border-radius: 4px;
    color: #fff; font-weight: 700; font-size: 20px; line-height: 31px; padding-left: 6px;
  }
  .hours-list {
    position: absolute; left: 38px; top: 698px; font-size: 16px; line-height: 17.5px; color: var(--text-dark); list-style: none;
  }

  .discount {
    position: absolute; left: 385px; top: 655px; width: 398px; height: 114px;
    background: linear-gradient(180deg, #f6f6f6, var(--panel-grey)); border-radius: 5px;
    font-family: "Oswald", "Arial Narrow", sans-serif; font-weight: 500; color: #666;
    text-align: center; font-size: 21px; line-height: 27px; padding-top: 8px;
    box-shadow: 0 8px 8px -4px rgba(0,0,0,.3);
  }
  .discount-big { font-size: 37px; line-height: 40px; color: var(--teal-dark); font-weight: 600; }

  .services-band {
    position: absolute; left: 0; top: 782px; width: 803px; height: 255px;
    border-top: 8px solid var(--teal);
    background: linear-gradient(180deg, var(--green-light), var(--green));
  }
  .services-title {
    position: absolute; left: 0; top: 22px; width: 803px; text-align: center;
    color: var(--teal-dark); font-weight: 700; font-size: 22px;
  }
  .services-list { position: absolute; top: 60px; list-style: none; font-size: 23px; line-height: 27.5px; color: var(--text-grey); }
  .services-list li { display: flex; align-items: center; gap: 12px; }
  .services-left { left: 73px; }
  .services-right { left: 432px; }
  .tick { width: 18px; height: 18px; flex: none; }
  .website {
    position: absolute; left: 0; top: 200px; width: 803px; text-align: center;
    color: #3d3d3d; font-weight: 700; font-size: 19px;
  }
</style>
</head>
<body>
<main class="flyer">
  <div class="hero-photo" role="img" aria-label="Close-up photograph of a bright white smile with soft blue flowers in the background"></div>

  <svg class="hero-shapes" viewBox="0 0 803 1037" aria-hidden="true">
    <path d="M478,0 Q640,150 580,360 L803,360 L803,0 Z" fill="var(--paper)"/>
    <path d="M478,0 Q640,150 580,360" fill="none" stroke="var(--green)" stroke-width="7"/>
    <path d="M0,392 Q430,250 803,342 L803,1037 L0,1037 Z" fill="var(--teal)"/>
    <path d="M0,405 Q430,268 803,358 L803,1037 L0,1037 Z" fill="var(--green)"/>
    <path d="M0,432 Q430,300 803,385 L803,1037 L0,1037 Z" fill="var(--paper)"/>
  </svg>

  <div class="brand">
    <span class="brand-dot"></span>
    <span class="brand-name">Crestline Dental Marbury</span>
  </div>

  <h1 class="headline">WE PUT<br>SMILE IN<br>YOUR LIFE</h1>

  <div class="offer-banner">WE OFFER COMFORTABLE AND<br>AFFORDABLE DENTAL CARE</div>

  <p class="intro intro-gap">NO GAP Checkup and Clean with any major Private Health Fund.<br>Includes oral exam, 2 X-Rays, Scale &amp; Polish and Fluoride Treatment</p>
  <p class="intro intro-family">Looking for a dentist office that is perfect for the entire family? From small children to seniors, we'll make sure each and every visit is pain free and enjoyable. We want you to love being in our office, just as much as we love serving our customers.</p>

  <p class="promise">WE JUST DON’T SAY BUT DELIVER OUR PROMISES!</p>

  <div class="hours-tag">Office Hours:</div>
  <ul class="hours-list">
    <li>Monday 8:30am – 5:30pm</li>
    <li>Tuesday 12:00pm – 8:00pm</li>
    <li>Wednesday – Friday 8:30am – 5:30pm</li>
    <li>Saturday 9:00am – 4:00pm</li>
  </ul>

  <div class="discount">
    <span class="discount-big">10% OFF</span> ON ALL MAJOR DENTAL.<br>
    INCLUDES FILLINGS, CROWNS, BRIDGES<br>
    AND ROOT CANAL TREATMENT
  </div>

  <section class="services-band">
    <h2 class="services-title">AVAILABLE DENTAL SERVICES AND PROCEDURES:</h2>
    <ul class="services-list services-left">
      <li><svg class="tick" viewBox="0 0 18 18"><path d="M2,10 L7,15 L16,2" fill="none" stroke="var(--tick-red)" stroke-width="3"/></svg>Checkup &amp; Clean</li>
      <li><svg class="tick" viewBox="0 0 18 18"><path d="M2,10 L7,15 L16,2" fill="none" stroke="var(--tick-red)" stroke-width="3"/></svg>Child Friendly Dentistry</li>
      <li><svg class="tick" viewBox="0 0 18 18"><path d="M2,10 L7,15 L16,2" fill="none" stroke="var(--tick-red)" stroke-width="3"/></svg>Crowns</li>
      <li><svg class="tick" viewBox="0 0 18 18"><path d="M2,10 L7,15 L16,2" fill="none" stroke="var(--tick-red)" stroke-width="3"/></svg>Dentures</li>
      <li><svg class="tick" viewBox="0 0 18 18"><path d="M2,10 L7,15 L16,2" fill="none" stroke="var(--tick-red)" stroke-width="3"/></svg>Extraction</li>
    </ul>
    <ul class="services-list services-right">
      <li><svg class="tick" viewBox="0 0 18 18"><path d="M2,10 L7,15 L16,2" fill="none" stroke="var(--tick-red)" stroke-width="3"/></svg>Root Canal Treatment</li>
      <li><svg class="tick" viewBox="0 0 18 18"><path d="M2,10 L7,15 L16,2" fill="none" stroke="var(--tick-red)" stroke-width="3"/></svg>Same Day Emergency</li>
      <li><svg class="tick" viewBox="0 0 18 18"><path d="M2,10 L7,15 L16,2" fill="none" stroke="var(--tick-red)" stroke-width="3"/></svg>Tooth Replacement (Bridges)</li>
      <li><svg class="tick" viewBox="0 0 18 18"><path d="M2,10 L7,15 L16,2" fill="none" stroke="var(--tick-red)" stroke-width="3"/></svg>White Fillings</li>
      <li><svg class="tick" viewBox="0 0 18 18"><path d="M2,10 L7,15 L16,2" fill="none" stroke="var(--tick-red)" stroke-width="3"/></svg>Whitening</li>
    </ul>
    <p class="website">www.crestlinedentalmarbury.com.au</p>
  </section>
</main>
</body>
</html>
```